VELTA CORE

I am in this industry for last 15 years we have done lots of commercial site like we work with BRAVEN costruction, lumo properties, TWD, penwick construction.
We do all domestic and commercial wall and floor tiling, swimming pools, spas, paving, marbles blue stones and muchmore.

Specializing in the wall and floor Tiling, Waterproofing and floor preparations

Industry/Entity Type

Industry

Number of Pages Required

1 page

Font styles to use
Serif
Decorative

Colors

Designer to choose colors to be used in the design.

Requirements
Must have
• domestic and commercial indoor tiling, bathroom tiling and paving pictures
Nice to have
• beautiful bathroom pictures with tile

```html
<!DOCTYPE html>
<html lang="en">
<head>
<meta charset="utf-8">
<title>VELTA CORE TILES</title>
<link href="https://fonts.googleapis.com/css2?family=Open+Sans:wght@400;600;700;800&family=Great+Vibes&display=swap" rel="stylesheet">
<style>
:root{
  --orange:#f47a20;
  --dark:#333333;
  --ink:#222222;
  --text:#555555;
  --grey:#e9e9e9;
  --icon:#5f6062;
  --line:#d6d6d6;
  --white:#ffffff;
}
*{margin:0;padding:0;box-sizing:border-box}
html,body{width:1200px;height:3586px;overflow:hidden;background:var(--white)}
body{position:relative;font-family:"Open Sans",Arial,sans-serif;color:var(--ink)}
.abs{position:absolute}
.photo{position:absolute;display:block}

/* header */
.site-header{position:absolute;left:0;top:0;width:1200px;height:105px;background:var(--white)}
.top-bar{position:absolute;right:110px;top:10px;display:flex;align-items:center;gap:22px;font-size:13px;color:var(--ink)}
.top-bar .phone{display:flex;align-items:center;gap:8px}
.top-bar svg{display:block}
.cart{position:relative}
.cart-count{position:absolute;top:-7px;right:-8px;width:13px;height:13px;border-radius:50%;background:var(--orange);color:#fff;font-size:8px;line-height:13px;text-align:center}
.brand{position:absolute;left:100px;top:52px;display:flex;align-items:center;gap:12px;font-weight:800;font-size:27px;letter-spacing:.3px;color:var(--ink)}
.brand-square{width:26px;height:26px;background:var(--orange)}
.main-nav{position:absolute;left:510px;top:64px;display:flex;gap:31px;font-size:13px;color:var(--ink)}
.main-nav .has-sub::after{content:"";display:inline-block;margin-left:4px;width:5px;height:5px;border-right:1px solid #777;border-bottom:1px solid #777;transform:rotate(45deg) translateY(-3px)}

/* hero */
.hero{position:absolute;left:0;top:105px;width:1200px;height:514px;background:linear-gradient(100deg,#cfc9c2 0%,#efece8 35%,#e2dad0 60%,#f3efe9 80%,#cbbfb0 100%)}
.hero-badge{position:absolute;top:164px;width:86px;height:86px}
.hero-badge .shape{position:absolute;left:13px;top:13px;width:60px;height:60px;background:#2c2c2c;transform:rotate(45deg);border-radius:6px}
.hero-badge .num{position:absolute;left:0;top:12px;width:86px;text-align:center;color:#fff;font-weight:700;font-size:30px}
.hero-badge .lbl{position:absolute;left:0;top:50px;width:86px;text-align:center;color:#fff;font-size:10px;font-weight:600}
.hero-title{position:absolute;left:167px;top:291px}
.hero-title .sub{font-size:25px;color:#111;letter-spacing:.5px}
.hero-title .main{font-size:31px;font-weight:800;color:#111;letter-spacing:.5px;margin-top:2px}
.hero-arrow{position:absolute;top:253px;width:24px;height:24px;border-radius:50%;background:rgba(255,255,255,.75);display:flex;align-items:center;justify-content:center}

/* section titles */
.section-title{position:absolute;left:0;width:1200px;text-align:center;font-size:25px;font-weight:600;color:var(--ink);letter-spacing:.3px}
.section-title::after{content:"";display:block;margin:8px auto 0;width:280px;height:2px;background:linear-gradient(90deg,var(--line) 0,var(--line) 38%,var(--orange) 38%,var(--orange) 62%,var(--line) 62%)}

/* product range */
.range-tile{position:absolute;width:320px;height:198px;display:flex;align-items:center;justify-content:center}
.range-tile span,.slide span{color:#fff;font-size:20px;font-weight:600;text-shadow:0 1px 3px rgba(0,0,0,.45);letter-spacing:.3px}

/* latest products */
.latest-band{position:absolute;left:0;top:1276px;width:1200px;height:416px;background:var(--grey)}
.slide{position:absolute;top:1341px;width:182px;height:289px;display:flex;align-items:center;justify-content:center}
.slider-nav{position:absolute;top:1297px;width:22px;height:20px;background:#fff;border:1px solid #ccc;display:flex;align-items:center;justify-content:center}

/* technical advice */
.advice-item{position:absolute;top:1826px;width:240px;text-align:center}
.advice-icon{margin:0 auto;width:172px;height:172px}
.advice-label{margin-top:20px;font-size:13px;font-weight:600;line-height:24px;color:var(--ink);padding:0 30px}

/* news */
.news-card{position:absolute;top:2246px;width:311px;text-align:center}
.news-meta{font-size:11px;font-weight:600;color:var(--ink)}
.news-photo{height:180px;margin-top:10px}
.news-title{margin-top:20px;font-size:13px;font-weight:700;line-height:20px;color:var(--ink)}
.news-text{margin-top:8px;font-size:12px;line-height:18px;color:var(--text)}
.btn-outline{display:inline-block;margin-top:18px;width:115px;height:36px;line-height:32px;border:2px solid #bbb;font-size:12px;font-weight:600;color:var(--ink)}

/* sample cards */
.sample-band{position:absolute;left:0;top:2689px;width:755px;height:406px;background:linear-gradient(115deg,#eeeae6 0%,#e2ddd6 40%,#f1eeea 70%,#dcd5cc 100%)}
.sample-title{position:absolute;left:100px;top:2737px;font-size:20px;font-weight:700;color:var(--ink)}
.sample-text{position:absolute;left:354px;top:2782px;width:290px;font-size:12px;line-height:19px;color:var(--text)}
.btn-dark{position:absolute;display:flex;align-items:center;justify-content:center;background:var(--dark);color:#fff;font-size:15px}

/* magazine */
.magazine{position:absolute;left:710px;top:2744px;width:490px;height:296px;background:var(--orange)}
.magazine::before{content:"";position:absolute;inset:8px;border:2px dashed rgba(255,255,255,.75)}
.mag-title{position:absolute;left:40px;top:28px;font-family:"Great Vibes",cursive;font-size:40px;color:#fff}
.mag-edition{position:absolute;left:40px;top:84px;font-size:13px;font-weight:700;color:#fff}
.mag-text{position:absolute;left:40px;top:106px;width:240px;font-size:11px;line-height:16px;color:#fff;text-align:center}
.mag-link{position:absolute;left:50px;top:236px;font-size:13px;color:#fff}

/* footer */
.site-footer{position:absolute;left:0;top:3155px;width:1200px;height:370px;background:var(--dark);color:#fff}
.footer-divider{position:absolute;top:30px;width:1px;height:310px;background:#555}
.footer-heading{position:absolute;font-size:15px;font-weight:600}
.footer-address{position:absolute;left:100px;top:218px;width:270px;text-align:center;font-size:12px;line-height:18px}
.newsletter-input{position:absolute;left:478px;top:112px;width:148px;height:43px;background:var(--orange);border-right:1px solid #e36a12;font-size:12px;line-height:43px;padding-left:14px}
.newsletter-btn{position:absolute;left:626px;top:112px;width:96px;height:43px;background:var(--orange);font-size:12px;line-height:43px;text-align:center}
.social{position:absolute;top:286px;left:521px;display:flex;gap:10px}
.social span{width:24px;height:24px;border:1px solid var(--orange)}
.quick-links{position:absolute;left:850px;top:116px;display:grid;grid-template-columns:116px 120px;row-gap:6px;font-size:13px}
.quick-links span::before{content:"";display:inline-block;width:6px;height:6px;border-top:2px solid var(--orange);border-right:2px solid var(--orange);transform:rotate(45deg);margin-right:8px;vertical-align:2px}
.footer-brand{position:absolute;left:837px;top:252px;display:flex;align-items:center;gap:10px;font-size:25px;font-weight:800}
.copyright{position:absolute;left:0;top:3525px;width:1200px;height:61px;background:var(--orange);color:#fff;font-size:11px;text-align:center;line-height:61px}
</style>
</head>
<body>

<header class="site-header">
  <div class="top-bar">
    <span class="phone">
      <svg width="16" height="16" viewBox="0 0 16 16"><circle cx="8" cy="8" r="8" fill="#222"/><path d="M5.2 4.2l1.4 1.6-.7 1c.5 1 1.2 1.7 2.2 2.2l1-.7 1.6 1.4-.9 1.2C7.6 10.8 5.2 8.4 4.1 5.2z" fill="#fff"/></svg>
      0800 765 4321
    </span>
    <svg width="14" height="14" viewBox="0 0 14 14"><circle cx="6" cy="6" r="4.3" fill="none" stroke="#222" stroke-width="2"/><path d="M9 9l4 4" stroke="#222" stroke-width="2"/></svg>
    <svg width="18" height="12" viewBox="0 0 18 12"><circle cx="6" cy="3.5" r="3" fill="#222"/><path d="M0 12c0-4 12-4 12 0z" fill="#222"/><path d="M14 5l2 2 2-2" stroke="#222" fill="none"/></svg>
    <span class="cart"><svg width="14" height="14" viewBox="0 0 14 14"><path d="M1 2h2l2 8h7l1.5-6H4" stroke="#222" stroke-width="1.6" fill="none"/><circle cx="6" cy="12.5" r="1.2" fill="#222"/><circle cx="11" cy="12.5" r="1.2" fill="#222"/></svg><span class="cart-count">0</span></span>
  </div>
  <div class="brand"><span class="brand-square"></span>VELTA CORE TILES</div>
  <nav class="main-nav">
    <span>HOME</span><span>ABOUT</span><span class="has-sub">PRODUCTS</span><span class="has-sub">LITERATURE</span><span>NEWS</span><span class="has-sub">ADVICE</span><span>CONTACT</span>
  </nav>
</header>

<section class="hero" role="img" aria-label="Bright open-plan dining room with polished stone and marble effect porcelain floor tiles">
  <div class="hero-badge" style="left:184px"><div class="shape"></div><div class="num">12</div><div class="lbl">COLOURS</div></div>
  <div class="hero-badge" style="left:311px"><div class="shape"></div><div class="num">1</div><div class="lbl">FINISH</div></div>
  <div class="hero-badge" style="left:443px"><div class="shape"></div><div class="num">8</div><div class="lbl">TILE SIZES</div></div>
  <div class="hero-title">
    <div class="sub">GLAZED PORCELAIN TILES</div>
    <div class="main">STONE &amp;MARBLE EFFECT</div>
  </div>
  <div class="hero-arrow" style="left:100px"><svg width="8" height="10" viewBox="0 0 8 10"><path d="M6 1L2 5l4 4" stroke="#333" stroke-width="1.5" fill="none"/></svg></div>
  <div class="hero-arrow" style="left:1071px"><svg width="8" height="10" viewBox="0 0 8 10"><path d="M2 1l4 4-4 4" stroke="#333" stroke-width="1.5" fill="none"/></svg></div>
</section>

<h2 class="section-title" style="top:660px">OUR PRODUCT RANGE</h2>
<div class="range-tile" style="left:98px;top:729px;background:linear-gradient(135deg,#8b7357,#d8cdbd 55%,#5a4532)" role="img" aria-label="Living room with porcelain floor tiles"><span>PROCELAIN</span></div>
<div class="range-tile" style="left:440px;top:729px;background:linear-gradient(135deg,#a9aba8,#dcdddb 60%,#bfc1be)" role="img" aria-label="Light grey ceramic floor tiles"><span>CERAMIC</span></div>
<div class="range-tile" style="left:782px;top:729px;background:linear-gradient(135deg,#8a8a86,#c9c8c2 50%,#4f5a52)" role="img" aria-label="Round mosaic tile floor inlay"><span>MOSAIC TILES</span></div>
<div class="range-tile" style="left:98px;top:951px;background:linear-gradient(135deg,#5d4e3e,#a89172 50%,#3f352c)" role="img" aria-label="Bathroom with natural stone wall cladding"><span>NATURAL STONE</span></div>
<div class="range-tile" style="left:440px;top:951px;background:linear-gradient(135deg,#6e6b66,#c8c4bd 50%,#3e3a35)" role="img" aria-label="Fireplace wall in reconstituted stone"><span>RECONSTITUTED STONE</span></div>
<div class="range-tile" style="left:782px;top:951px;background:linear-gradient(160deg,#7fa2c4,#d7c68a 50%,#6e7a48)" role="img" aria-label="House facade with dry fix brick slip system"><span>DRY FIX SYSTEMS</span></div>

<h2 class="section-title" style="top:1191px">LATEST PRODUCTS</h2>
<div class="latest-band"></div>
<div class="slider-nav" style="left:1050px"><svg width="6" height="8" viewBox="0 0 6 8"><path d="M5 1L2 4l3 3" stroke="#333" fill="none"/></svg></div>
<div class="slider-nav" style="left:1076px"><svg width="6" height="8" viewBox="0 0 6 8"><path d="M1 1l3 3-3 3" stroke="#333" fill="none"/></svg></div>
<div class="slide" style="left:98px;background:linear-gradient(180deg,#d9d4cc 0%,#c5bfb5 55%,#2e6d8c 100%)" role="img" aria-label="Pool edge paved with light stone tiles"><span>CORVANO</span></div>
<div class="slide" style="left:303px;background:linear-gradient(180deg,#2b3a52 0%,#7d6a52 50%,#c7b89e 100%)" role="img" aria-label="Outdoor terrace with porcelain paving at dusk"><span>TERRAZZA 20</span></div>
<div class="slide" style="left:508px;background:linear-gradient(180deg,#c9cdd0 0%,#b59a83 45%,#a88b72 100%)" role="img" aria-label="Sandstone effect outdoor paving slabs"><span>PIETRELLO 20</span></div>
<div class="slide" style="left:713px;background:linear-gradient(135deg,#6c716d,#8a8f8a 50%,#5a5e5b)" role="img" aria-label="Dark grey large format floor tiles"><span>ARDENA 20</span></div>
<div class="slide" style="left:918px;background:linear-gradient(180deg,#e8e6e2 0%,#d6d3ce 60%,#b9b6b1 100%)" role="img" aria-label="Bathroom with light porcelain wall and floor tiles"><span>CORVANO</span></div>

<h2 class="section-title" style="top:1731px">TECHNICAL ADVICE</h2>
<div class="advice-item" style="left:93px">
  <svg class="advice-icon" viewBox="0 0 172 172" role="img" aria-label="Shoe on tile icon"><rect x="36" y="36" width="100" height="100" rx="14" transform="rotate(45 86 86)" fill="var(--icon)"/><rect x="58" y="58" width="56" height="56" transform="rotate(45 86 86)" fill="none" stroke="#fff" stroke-width="2"/></svg>
  <div class="advice-label">SLIP RESISTANCE ADVICE FOR SHOD</div>
</div>
<div class="advice-item" style="left:348px">
  <svg class="advice-icon" viewBox="0 0 172 172" role="img" aria-label="Slippers on tile icon"><rect x="36" y="36" width="100" height="100" rx="14" transform="rotate(45 86 86)" fill="var(--icon)"/><rect x="58" y="58" width="56" height="56" transform="rotate(45 86 86)" fill="none" stroke="#fff" stroke-width="2"/></svg>
  <div class="advice-label">SLIP RESISTANCE ADVICE FOR SHOD</div>
</div>
<div class="advice-item" style="left:604px">
  <svg class="advice-icon" viewBox="0 0 172 172" role="img" aria-label="Abrasion wheel icon"><rect x="36" y="36" width="100" height="100" rx="14" transform="rotate(45 86 86)" fill="var(--icon)"/><circle cx="86" cy="86" r="24" fill="none" stroke="#fff" stroke-width="2"/><circle cx="86" cy="86" r="6" fill="#fff"/></svg>
  <div class="advice-label">PEI RATINGS ADVICE</div>
</div>
<div class="advice-item" style="left:860px">
  <svg class="advice-icon" viewBox="0 0 172 172" role="img" aria-label="Sun over tile icon"><rect x="36" y="36" width="100" height="100" rx="14" transform="rotate(45 86 86)" fill="var(--icon)"/><circle cx="86" cy="78" r="12" fill="none" stroke="#fff" stroke-width="2"/><g stroke="#fff" stroke-width="2"><path d="M86 56v8M86 92v8M64 78h8M100 78h8M70 62l6 6M96 88l6 6M102 62l-6 6M70 94l6-6"/></g></svg>
  <div class="advice-label">LRV ADVICE</div>
</div>

<h2 class="section-title" style="top:2143px">NEWS &amp; EVENTS</h2>
<article class="news-card" style="left:98px">
  <div class="news-meta">SEPTEMBER 5, 2017 | 7 COMMENTS</div>
  <div class="news-photo" style="background:linear-gradient(135deg,#9fc7c9,#e8f1f1 50%,#6aa3a6)" role="img" aria-label="Glass shower enclosure with mosaic tiles"></div>
  <h3 class="news-title">CRAS LIGULA MASSA, EFFICITUR CONDI-<br>MENTUM TEMPUS NEC</h3>
  <p class="news-text">Lorem ipsum dolor sit amet, consectetur adipiscing elit. Cras ligula massa, efficitur condimentum tempus nec, volutpat eget quam...</p>
  <span class="btn-outline">VIEW MORE</span>
</article>
<article class="news-card" style="left:445px">
  <div class="news-meta">SEPTEMBER 5, 2017 | 7 COMMENTS</div>
  <div class="news-photo" style="background:linear-gradient(180deg,#c7cbcc,#eceeee 45%,#8c6a4a)" role="img" aria-label="Bathroom vanity with tiled wall and plants"></div>
  <h3 class="news-title">CRAS LIGULA MASSA, EFFICITUR CONDI-<br>MENTUM TEMPUS NEC</h3>
  <p class="news-text">Lorem ipsum dolor sit amet, consectetur adipiscing elit. Cras ligula massa, efficitur condimentum tempus nec, volutpat eget quam...</p>
  <span class="btn-outline">VIEW MORE</span>
</article>
<article class="news-card" style="left:791px">
  <div class="news-meta">SEPTEMBER 5, 2017 | 7 COMMENTS</div>
  <div class="news-photo" style="background:linear-gradient(135deg,#b7aa9a,#e6e0d8 50%,#8f8172)" role="img" aria-label="Modern bathroom with stone effect tiles"></div>
  <h3 class="news-title">CRAS LIGULA MASSA, EFFICITUR CONDI-<br>MENTUM TEMPUS NEC</h3>
  <p class="news-text">Lorem ipsum dolor sit amet, consectetur adipiscing elit. Cras ligula massa, efficitur condimentum tempus nec, volutpat eget quam...</p>
  <span class="btn-outline">VIEW MORE</span>
</article>

<section>
  <div class="sample-band" role="img" aria-label="Soft marble tile background"></div>
  <h3 class="sample-title">REQUEST A5 SAMPLE CARDS</h3>
  <div class="photo" style="left:100px;top:2796px;width:223px;height:275px;background:linear-gradient(160deg,#3d3f45,#8b8d92 45%,#e9e9ea 100%)" role="img" aria-label="Stack of A5 tile sample cards"></div>
  <p class="sample-text">Lorem ipsum dolor sit amet, consectetur adipiscing elit. Cras ligula massa, efficitur condimentum tempus nec, volutpat eget quam. Fusce sagittis sapien ut libero dignissim eleifend. Proin at amet mauris nec orci feugiat faucibus. Nullam laoreet tortor nibh, in vel maximus dolor. Fusce varius mi finibus magna euis mod pharetra. Suspendisse non lacinia quam, eu semper nisl. Maecenas risus ipsum, semper eget fer mentum vel, efficitur et sem. Aliquam a augue non diam rhoncus imperdiet. Donec sem nunc, viverra in</p>
  <span class="btn-dark" style="left:354px;top:3004px;width:143px;height:41px">Request Now !</span>
</section>

<aside class="magazine">
  <div class="mag-title">Latest Magazine</div>
  <div class="mag-edition">Surface Journal SDS 16 edition</div>
  <p class="mag-text">Lorem ipsum dolor sit amet, consectetur adipiscing elit. Cras ligula massa, efficitur condimentum tempus nec</p>
  <span class="btn-dark" style="left:76px;top:184px;width:163px;height:36px;font-size:14px">Request a Magazine!</span>
  <span class="mag-link">View online version</span>
  <div class="photo" style="left:301px;top:19px;width:167px;height:248px;background:linear-gradient(180deg,#1c1c1c 0%,#2b2b2b 22%,#7a6552 55%,#3a3129 100%)" role="img" aria-label="Magazine cover showing a tiled living space"></div>
</aside>

<footer class="site-footer">
  <div class="photo" style="left:170px;top:72px;width:134px;height:131px;background:linear-gradient(135deg,#e4e6df,#f4f3ee 50%,#d7dccf);border:3px solid #fff" role="img" aria-label="Location map"></div>
  <div class="footer-address"><strong style="font-weight:400;font-size:15px">USA</strong><br>123-Lorem ipsum dolor sit amet,<br>consectetur adipiscing elit<br>Tel: 0800 765 4321</div>
  <div class="footer-divider" style="left:435px"></div>
  <div class="footer-divider" style="left:813px"></div>
  <div class="footer-heading" style="left:486px;top:72px">Subscribe for our Newsletter</div>
  <div class="newsletter-input">Email Address</div>
  <div class="newsletter-btn">Subscribe</div>
  <div class="abs" style="left:478px;top:198px;width:244px;height:1px;background:#555"></div>
  <div class="footer-heading" style="left:556px;top:246px">Follow Us</div>
  <div class="social"><span aria-label="Social link"></span><span aria-label="Social link"></span><span aria-label="Social link"></span><span aria-label="Social link"></span></div>
  <div class="footer-heading" style="left:932px;top:72px">Quick links</div>
  <div class="quick-links">
    <span>Home</span><span>Literature</span>
    <span>About Us</span><span>Advice</span>
    <span>Products</span><span>Contact</span>
  </div>
  <div class="footer-brand"><span class="brand-square"></span>VELTA CORE TILES</div>
</footer>
<div class="copyright">Copyright © 20017 veltacoretiles.com. All Rights Reserved</div>

</body>
</html>
```